Creative & Professional Business Card for hair salon

We are looking to update our business cards. Our salon is creative, modern, progressive and professional and looking for a design that will reflect this.

```html
<!DOCTYPE html>
<html lang="en">
<head>
<meta charset="utf-8">
<title>Silver Lining Studio – Business Cards</title>
<link rel="stylesheet" href="https://fonts.googleapis.com/css2?family=Montserrat:wght@400;600;700&display=swap">
<style>
  :root {
    --backdrop: #e6e8e9;
    --card-blue: #8fbac9;
    --card-blue-light: #9ec5d2;
    --card-ink: #ffffff;
    --brand-blue: #4f8fa8;
    --card-shadow: rgba(40, 60, 70, 0.18);
  }
  html, body {
    margin: 0;
    padding: 0;
    width: 1200px;
    height: 873px;
    overflow: hidden;
    background: var(--backdrop);
  }
  .stage {
    position: relative;
    width: 1200px;
    height: 873px;
    font-family: "Montserrat", Arial, sans-serif;
  }
  .card-slot {
    position: absolute;
    top: 116px;
    width: 366px;
    height: 640px;
  }
  .card-slot--back { left: 200px; }
  .card-slot--front { left: 634px; }
  .card {
    position: absolute;
    top: 0;
    left: 0;
    width: 640px;
    height: 366px;
    transform-origin: top left;
    transform: translateX(366px) rotate(90deg);
    background: linear-gradient(135deg, var(--card-blue-light), var(--card-blue));
    box-shadow: 6px -6px 18px var(--card-shadow);
    border-radius: 4px;
    overflow: hidden;
  }

  /* Contact side */
  .contact-name {
    position: absolute;
    left: 44px;
    top: 44px;
    margin: 0;
    color: var(--card-ink);
    font-weight: 700;
    font-size: 24px;
    letter-spacing: 1.5px;
    text-transform: uppercase;
  }
  .contact-role {
    position: absolute;
    left: 44px;
    top: 78px;
    margin: 0;
    color: var(--card-ink);
    font-weight: 400;
    font-size: 17px;
  }
  .contact-rule {
    position: absolute;
    left: 200px;
    top: 208px;
    width: 410px;
    height: 2px;
    background: var(--card-ink);
  }
  .contact-divider {
    position: absolute;
    left: 236px;
    top: 168px;
    width: 2px;
    height: 112px;
    background: var(--card-ink);
  }
  .contact-phone {
    position: absolute;
    left: 252px;
    top: 176px;
    margin: 0;
    color: var(--card-ink);
    font-weight: 700;
    font-size: 22px;
    letter-spacing: 1px;
  }
  .contact-web {
    position: absolute;
    left: 252px;
    top: 218px;
    margin: 0;
    color: var(--card-ink);
    font-weight: 400;
    font-size: 18px;
  }

  /* Brand side */
  .brand {
    position: absolute;
    left: 0;
    right: 0;
    top: 136px;
    display: flex;
    align-items: center;
    justify-content: center;
    gap: 16px;
  }
  .brand-dot {
    width: 22px;
    height: 22px;
    border-radius: 50%;
    background: var(--brand-blue);
  }
  .brand-name {
    margin: 0;
    color: var(--brand-blue);
    font-weight: 600;
    font-size: 40px;
    letter-spacing: 2px;
    text-transform: uppercase;
  }
</style>
</head>
<body>
  <main class="stage">
    <div class="card-slot card-slot--back">
      <section class="card card--contact" aria-label="Business card, contact side">
        <h1 class="contact-name">Mara Lenhart</h1>
        <p class="contact-role">Founder and CEO</p>
        <div class="contact-rule"></div>
        <div class="contact-divider"></div>
        <p class="contact-phone">xxx•xxx•xxxx</p>
        <p class="contact-web">www.silverliningstudio.com</p>
      </section>
    </div>

    <div class="card-slot card-slot--front">
      <section class="card card--brand" aria-label="Business card, brand side">
        <div class="brand">
          <span class="brand-dot"></span>
          <h2 class="brand-name">Silver Lining Studio</h2>
        </div>
      </section>
    </div>
  </main>
</body>
</html>
```